Corporate Brightfen business cards to be handed to investor, bankers etc. Needs to have a young feel

I need business cards designed for a technology company that provides uber-like rapid response on the security industry. I would like it simple but very cool and tasteful. See attached documents for artwork and colours to be used. Cut sheet describes business model. Card stock should be thicker than normal. I would like the one side to be just the art and the other to have the contact info with maybe the pin somewhere.

Target Market(s)

Investors

Industry/Entity Type

Business

Contact Information for Business Card

Would like the logo attached on one side with name address and other info on the other side.

Font styles to use
Other font styles liked:
• See existing logo

Colors
6b449b
886aae
e4daeb
ffffff

Requirements
Must have
• Name: Dorian Felkatsis
• Address: 47 Larkfield Avenue, Toronto, On, M6K2B7
• Tel: 416-7291846
• Email: rolo@brightfen.io
Nice to have
• See logo colours

```html
<!DOCTYPE html>
<html lang="en">
<head>
<meta charset="utf-8">
<title>Brightfen business cards</title>
<link rel="stylesheet" href="https://fonts.googleapis.com/css2?family=Quicksand:wght@400;500;700&display=swap">
<style>
  :root {
    --page: #ebe8ef;
    --purple-deep: #553592;
    --purple-front-a: #5a3a9a;
    --purple-front-b: #7b4ba8;
    --purple-mid: #6b449b;
    --lavender: #886aae;
    --lavender-pale: #e4daeb;
    --white: #ffffff;
    --accent-green: #7bbf3a;
  }
  * { margin: 0; padding: 0; box-sizing: border-box; }
  html, body {
    width: 1200px;
    height: 1200px;
    overflow: hidden;
    background: var(--page);
    font-family: "Quicksand", sans-serif;
  }
  .sheet {
    width: 1200px;
    height: 1200px;
    display: flex;
    flex-direction: column;
    align-items: center;
    gap: 44px;
    padding-top: 45px;
  }
  .card {
    position: relative;
    width: 880px;
    height: 533px;
    overflow: hidden;
    box-shadow: 0 6px 18px rgba(40, 20, 70, 0.22);
    color: var(--white);
  }

  /* Art side */
  .card--art {
    background: linear-gradient(100deg, var(--purple-front-a) 0%, var(--purple-mid) 55%, var(--purple-front-b) 100%);
  }
  .art-field {
    position: absolute;
    inset: 0;
    background: radial-gradient(ellipse 60% 70% at 58% 60%, rgba(136, 106, 174, 0.45) 0%, rgba(136, 106, 174, 0.18) 50%, rgba(136, 106, 174, 0) 100%);
  }
  .card--art .brand {
    position: absolute;
    left: 0;
    right: 0;
    top: 228px;
    text-align: center;
  }

  /* Company name */
  .brand__name {
    font-weight: 500;
    font-size: 64px;
    line-height: 1;
    color: var(--white);
  }

  /* Contact side */
  .card--contact { background: var(--purple-deep); }
  .card--contact .brand {
    position: absolute;
    left: 38px;
    top: 46px;
  }
  .holder {
    position: absolute;
    left: 490px;
    top: 196px;
    right: 0;
  }
  .holder__name {
    font-size: 27px;
    padding-left: 8px;
    padding-bottom: 4px;
    font-weight: 500;
  }
  .holder__name strong { font-weight: 700; }
  .holder__rule {
    height: 4px;
    background: var(--accent-green);
    border-radius: 2px 0 0 2px;
  }
  .contact-list {
    position: absolute;
    left: 36px;
    top: 326px;
    list-style: none;
  }
  .contact-list__item {
    display: flex;
    align-items: center;
    gap: 16px;
    height: 62px;
    font-size: 24px;
    font-weight: 500;
  }
  .contact-list__icon { width: 36px; height: 40px; flex: none; }
</style>
</head>
<body>
<main class="sheet">

  <section class="card card--art" aria-label="Card art side">
    <div class="art-field" role="img" aria-label="Faint illustration of a storefront with a padlock and security service icons"></div>
    <div class="brand">
      <span class="brand__name">Brightfen</span>
    </div>
  </section>

  <section class="card card--contact" aria-label="Card contact side">
    <div class="brand">
      <span class="brand__name">Brightfen</span>
    </div>

    <div class="holder">
      <p class="holder__name"><strong>Dorian</strong> Felkatsis</p>
      <div class="holder__rule"></div>
    </div>

    <ul class="contact-list">
      <li class="contact-list__item">
        <svg class="contact-list__icon" viewBox="0 0 36 40" aria-hidden="true">
          <polygon points="18,2 33,11 33,29 18,38 3,29 3,11" fill="none" stroke="#7bbf3a" stroke-width="2"/>
          <path d="M13 12 l3 0 l2 5 l-2 1.5 a10 10 0 0 0 4.5 4.5 l1.5 -2 l5 2 l0 3 a2 2 0 0 1 -2 2 a16 16 0 0 1 -14 -14 a2 2 0 0 1 2 -2z" fill="#ffffff" transform="translate(-2,-1) scale(0.95)"/>
        </svg>
        <span>47 Larkfield Avenue, Toronto, On, M6K2B7</span>
      </li>
      <li class="contact-list__item">
        <svg class="contact-list__icon" viewBox="0 0 36 40" aria-hidden="true">
          <polygon points="18,2 33,11 33,29 18,38 3,29 3,11" fill="none" stroke="#7bbf3a" stroke-width="2"/>
          <rect x="10" y="14" width="16" height="12" rx="1" fill="none" stroke="#ffffff" stroke-width="2"/>
          <path d="M10 14 l8 7 l8 -7" fill="none" stroke="#ffffff" stroke-width="2"/>
        </svg>
        <span>416-7291846</span>
      </li>
      <li class="contact-list__item">
        <svg class="contact-list__icon" viewBox="0 0 36 40" aria-hidden="true">
          <polygon points="18,2 33,11 33,29 18,38 3,29 3,11" fill="none" stroke="#7bbf3a" stroke-width="2"/>
          <circle cx="18" cy="20" r="8" fill="none" stroke="#ffffff" stroke-width="1.8"/>
          <ellipse cx="18" cy="20" rx="3.5" ry="8" fill="none" stroke="#ffffff" stroke-width="1.5"/>
          <line x1="10" y1="20" x2="26" y2="20" stroke="#ffffff" stroke-width="1.5"/>
        </svg>
        <span>rolo@brightfen.io</span>
      </li>
    </ul>
  </section>

</main>
</body>
</html>
```